Graphic Design/Logo Needed for Ear Drops Bottle

We have an Ear Drop Medication that we need to create a new label for. We will use a retro picture of a Doctor (Dr. Halvane) and the name of the product is Mighty Lobe. There is no official logo, so we will want to create a retro, basic logo for Mighty Lobe and use the retro picture. Front portion of the label is Size is 1.5" in height, and about 1.375" Width. this is a small tube similar in size to eye drops. We will be looking for just the logo portion and what you will see on the front of the bottle.

Target Market(s)

Medical Container

Industry/Entity Type

Medical

Font styles to use
Serif
Sans Serif

Colors
0054AA
0677BA
7BADD7
CADEEF
E8F1F8
FFF300
FFF600
FEFA6F
FFFEC7
FFFEE8

Requirements
Must have
• Picture of Dr. Halvane, "Mighty Lobe", Dr. Halvane's Ear Solution
Nice to have
• Retro Style or Modern with Retro Feel, Clean and engaging

```html
<!DOCTYPE html>
<html lang="en">
<head>
<meta charset="utf-8">
<title>Mighty Lobe – Dr. Halvane's Ear Solution label</title>
<link rel="stylesheet" href="https://fonts.googleapis.com/css2?family=Cinzel:wght@700&family=Oswald:wght@600&family=Libre+Baskerville:wght@400&display=swap">
<style>
  :root {
    --backdrop: #ecebe8;
    --paper: #f8edc6;
    --paper-edge: #f1dfa8;
    --ink: #4f5054;
    --ink-soft: #6b6c70;
    --ribbon: #55575b;
    --ribbon-fold: #3c3d40;
    --cream-text: #f1e4bd;
    --photo-light: #efe6d0;
    --photo-dark: #b7a88c;
  }
  html, body {
    margin: 0;
    width: 1200px;
    height: 1200px;
    overflow: hidden;
    background: var(--backdrop);
  }
  .canvas {
    position: relative;
    width: 1200px;
    height: 1200px;
  }
  .label {
    position: absolute;
    left: 262px;
    top: 30px;
    width: 676px;
    height: 1140px;
    background: radial-gradient(ellipse at 50% 45%, var(--paper) 55%, var(--paper-edge) 100%);
  }
  .artwork {
    position: absolute;
    inset: 0;
  }
  .tagline {
    font-family: "Oswald", "Arial Narrow", sans-serif;
    font-weight: 600;
    font-size: 26px;
    letter-spacing: 3px;
    fill: var(--ink);
  }
  .product-name {
    font-family: "Cinzel", Georgia, serif;
    font-weight: 700;
    font-size: 58px;
    letter-spacing: 1px;
    fill: var(--cream-text);
  }
  .established {
    font-family: "Libre Baskerville", Georgia, serif;
    font-weight: 400;
    font-size: 22px;
    fill: var(--ink);
  }
  .solution-line {
    font-family: "Oswald", "Arial Narrow", sans-serif;
    font-weight: 600;
    font-size: 24px;
    letter-spacing: 0.5px;
    fill: var(--ink);
  }
  .photo-caption {
    font-family: "Oswald", "Arial Narrow", sans-serif;
    font-weight: 600;
    font-size: 11px;
    fill: #2f2f30;
  }
</style>
</head>
<body>
<main class="canvas">
  <section class="label">
    <svg class="artwork" viewBox="262 30 676 1140" width="676" height="1140" xmlns="http://www.w3.org/2000/svg">
      <defs>
        <linearGradient id="portrait-tone" x1="0" y1="0" x2="0" y2="1">
          <stop offset="0" stop-color="var(--photo-light)"/>
          <stop offset="1" stop-color="var(--photo-dark)"/>
        </linearGradient>
        <path id="tagline-arc" d="M378,440 A222,222 0 0 1 822,440"/>
        <path id="name-curve" d="M290,836 Q600,788 910,836"/>
        <path id="solution-arc" d="M420,830 A180,180 0 0 0 780,830"/>
      </defs>

      <!-- arch frame -->
      <g class="frame" fill="none" stroke="var(--ink)">
        <path d="M335,800 L335,440 A265,265 0 0 1 865,440 L865,800" stroke-width="5"/>
        <path d="M347,800 L347,440 A253,253 0 0 1 853,440 L853,800" stroke-width="2"/>
      </g>

      <!-- side dots -->
      <g stroke="var(--ink-soft)" stroke-width="7" stroke-linecap="round" stroke-dasharray="0 14">
        <line x1="381" y1="470" x2="381" y2="750"/>
        <line x1="819" y1="470" x2="819" y2="750"/>
      </g>

      <!-- portrait -->
      <path d="M415,790 L415,440 A185,185 0 0 1 785,440 L785,790 Z"
            fill="url(#portrait-tone)" stroke="var(--ink)" stroke-width="2"
            role="img" aria-label="Retro sepia portrait of Dr. Halvane in a white coat and tie with a head mirror, set against a sunburst"/>
      <text class="photo-caption" x="775" y="748" text-anchor="end">DR. HALVANE</text>

      <!-- tagline on arch -->
      <text class="tagline" text-anchor="middle">
        <textPath href="#tagline-arc" startOffset="50%">GENTLE CARE FOR EVERY EAR</textPath>
      </text>

      <!-- lower seal -->
      <g class="seal" fill="none" stroke="var(--ink)">
        <path d="M410,830 A190,190 0 0 0 790,830" stroke-width="5"/>
        <path d="M450,830 A150,150 0 0 0 750,830" stroke-width="2"/>
      </g>

      <!-- ribbon -->
      <g class="ribbon">
        <path d="M268,800 L312,790 L312,880 L268,890 L288,845 Z" fill="var(--ribbon-fold)"/>
        <path d="M932,800 L888,790 L888,880 L932,890 L912,845 Z" fill="var(--ribbon-fold)"/>
        <path d="M290,780 Q600,730 910,780 L910,878 Q600,828 290,878 Z" fill="var(--ribbon)"/>
      </g>
      <text class="product-name" text-anchor="middle">
        <textPath href="#name-curve" startOffset="50%">MIGHTY LOBE</textPath>
      </text>

      <!-- established line -->
      <text class="established" x="548" y="922" text-anchor="middle">ESTD</text>
      <text class="established" x="656" y="922" text-anchor="middle">1995</text>
      <path d="M600,900 L606,908 L616,914 L606,920 L600,928 L594,920 L584,914 L594,908 Z" fill="var(--ink)"/>
      <g fill="var(--ink)">
        <path d="M432,893 l3,7 7,0 -6,4 2,7 -6,-4 -6,4 2,-7 -6,-4 7,0 Z"/>
        <path d="M768,893 l3,7 7,0 -6,4 2,7 -6,-4 -6,4 2,-7 -6,-4 7,0 Z"/>
      </g>

      <!-- solution line on seal -->
      <text class="solution-line" text-anchor="middle">
        <textPath href="#solution-arc" startOffset="50%">DR. HALVANE'S EAR SOLUTION</textPath>
      </text>
    </svg>
  </section>
</main>
</body>
</html>
```